App landing page and Amber Nook template

I am building a web-based app to help people manage their lives. The app divides their life into 4 categories, Self, Relationships, Career, and Finance. I need a landing page for this application which will feature as a dashboard for each of the categories. The page will be dynamically updated as updates are received from the app. The logo will be a key feature of the page. There will be a menu to the left-hand side. A banner at the top will include interactive icons for the user to navigate the site, manage their account and logout.
I also need a template page for users to present the Ambers Nook to the end users where users can store passwords, important documents, and other important information. This template will present Secrets in either a list format or in an itemized box format.
I have attached the Application Logo for reference.

```html
<!DOCTYPE html>
<html lang="en">
<head>
<meta charset="utf-8">
<title>Amber Nook – Dashboard</title>
<link href="https://fonts.googleapis.com/css2?family=Outfit:wght@300;400;500;600&display=swap" rel="stylesheet">
<style>
:root{
  --ink:#1c2a4a;
  --muted:#8a93a6;
  --line:#e6e9ef;
  --brand:#0b5fa0;
  --brand-ink:#ffffff;
  --stage-top:#f5f5f6;
  --stage:#ffffff;
  --frame:#17191d;
  --card:#ffffff;
  --green:#25a244;
  --icon-blue:#1a5ea8;
  --icon-gold:#f2c230;
}
*{box-sizing:border-box;margin:0;padding:0}
html,body{width:801px;height:1200px;overflow:hidden}
body{font-family:"Outfit",sans-serif;color:var(--ink);background:var(--stage);position:relative}
.stage-band{position:absolute;left:0;top:0;width:801px;height:368px;background:var(--stage-top)}
.brand-mark{position:absolute;top:72px;left:0;width:801px;display:flex;justify-content:center;align-items:center;gap:10px}
.brand-mark .dot{width:22px;height:22px;border-radius:50%;background:var(--brand)}
.brand-mark .name{font-size:28px;font-weight:500;color:var(--brand)}

.dashboard{position:absolute;left:52px;width:697px;height:465px;border:2px solid var(--frame);border-radius:9px;background:#fff;overflow:hidden}
.dashboard.light{top:183px}
.dashboard.brand{top:686px}

.topbar{position:absolute;left:0;top:0;width:100%;height:42px;display:flex;align-items:center;border-bottom:1px solid var(--line)}
.topbar .logo-slot{width:40px;height:42px;display:flex;align-items:center;justify-content:center;font-size:5.5px;line-height:6px;font-weight:500;color:var(--brand);text-align:center}
.greeting{margin-left:8px}
.greeting .hello{font-size:9px;font-weight:300}
.greeting .hello b{font-weight:500}
.greeting .sub{font-size:5px;color:var(--muted);margin-top:1px}
.search{position:absolute;left:422px;top:11px;width:159px;height:20px;border:1px solid var(--line);border-radius:10px;font-size:5px;color:var(--muted);display:flex;align-items:center;padding:0 7px;justify-content:space-between}
.bell{position:absolute;left:589px;top:11px;width:20px;height:20px;border:1px solid var(--line);border-radius:50%;display:flex;align-items:center;justify-content:center}
.avatar{position:absolute;left:617px;top:11px;width:20px;height:20px;border-radius:50%;background:linear-gradient(135deg,#6b4a3a,#2b2020)}
.user-name{position:absolute;left:645px;top:17px;font-size:5.5px;font-weight:500}
.chev{position:absolute;left:682px;top:18px}

.sidebar{position:absolute;left:0;top:42px;width:40px;bottom:0;border-right:1px solid var(--line)}
.side-icon{position:absolute;left:10px;width:20px;height:14px;display:flex;align-items:center;justify-content:center}
.side-icon svg{width:10px;height:10px;stroke:#b3bccb;fill:none;stroke-width:1.6}
.side-icon.active svg{stroke:var(--brand)}
.active-tick{position:absolute;left:40px;top:20px;width:1px;height:10px;background:var(--icon-gold)}

.content{position:absolute;left:40px;top:42px;right:0;padding:16px 9px 0 11px}
.section{margin-bottom:16px}
.section-head{height:20px;display:flex;align-items:center;gap:14px}
.section-title{font-size:11px;font-weight:400;white-space:nowrap}
.section-rule{flex:1;height:1px;background:var(--line)}
.progress{height:13px;padding:0 6px;border:1px solid var(--line);border-radius:7px;display:flex;align-items:center;gap:4px;font-size:5.5px;font-weight:600;color:var(--green)}
.cards{margin-top:10px;display:grid;grid-template-columns:repeat(4,1fr);gap:8px}
.card{height:48px;background:var(--card);box-shadow:0 1px 4px rgba(20,40,80,.08);display:flex;align-items:center;gap:10px;padding-left:12px}
.card.highlight{background:linear-gradient(90deg,#e6eef6,#fbf7e8)}
.card .art{width:33px;height:27px;border-radius:3px;background:linear-gradient(135deg,rgba(26,94,168,.28),rgba(242,194,48,.35));flex:none}
.card .label{font-size:8.5px;line-height:9px;font-weight:300}

.footer{position:absolute;left:40px;right:0;top:419px;border-top:1px solid var(--line);padding:10px 0 0 11px;font-size:5px;color:var(--muted)}

/* branded variant */
.dashboard.brand .topbar,.dashboard.brand .sidebar{background:var(--brand);border-color:var(--brand)}
.dashboard.brand .topbar .logo-slot{background:#fff}
.dashboard.brand .greeting,.dashboard.brand .greeting .sub,.dashboard.brand .user-name{color:var(--brand-ink)}
.dashboard.brand .search{border-color:rgba(255,255,255,.7);color:#d8e6f3}
.dashboard.brand .bell{border-color:rgba(255,255,255,.7)}
.dashboard.brand .side-icon svg{stroke:#fff}
.dashboard.brand .side-icon.active{left:3px;width:37px;background:#fff;border-radius:7px 0 0 7px}
.dashboard.brand .side-icon.active svg{stroke:var(--brand)}
</style>
</head>
<body>
<svg width="0" height="0" style="position:absolute">
  <symbol id="i-grid" viewBox="0 0 12 12"><rect x="1" y="1" width="4" height="4" rx="1.5"/><rect x="7" y="1" width="4" height="4" rx="1.5"/><rect x="1" y="7" width="4" height="4" rx="1.5"/><rect x="7" y="7" width="4" height="4" rx="1.5"/></symbol>
  <symbol id="i-pie" viewBox="0 0 12 12"><path d="M6 2a4.5 4.5 0 1 0 4.5 4.5H6z"/><path d="M7.5 1v4h4a4 4 0 0 0-4-4z"/></symbol>
  <symbol id="i-cal" viewBox="0 0 12 12"><rect x="1" y="2" width="10" height="9" rx="1.5"/><path d="M1 5h10M4 1v2M8 1v2"/></symbol>
  <symbol id="i-doc" viewBox="0 0 12 12"><path d="M2.5 1h5l2.5 2.5V11h-7.5z"/><path d="M4.5 6h3M4.5 8h3"/></symbol>
  <symbol id="i-box" viewBox="0 0 12 12"><rect x="1" y="1.5" width="10" height="9" rx="1.5"/><path d="M1 4h10M4 6.5h4"/></symbol>
  <symbol id="i-gear" viewBox="0 0 12 12"><circle cx="6" cy="6" r="1.8"/><path d="M6 1v1.5M6 9.5V11M1 6h1.5M9.5 6H11M2.5 2.5l1 1M8.5 8.5l1 1M2.5 9.5l1-1M8.5 3.5l1-1"/></symbol>
  <symbol id="i-user" viewBox="0 0 12 12"><circle cx="6" cy="4" r="2.3"/><path d="M1.5 11a4.5 4.5 0 0 1 9 0"/></symbol>
  <symbol id="i-power" viewBox="0 0 12 12"><path d="M6 1v4.5"/><path d="M3.2 3a4 4 0 1 0 5.6 0"/></symbol>
</svg>

<div class="stage-band"></div>
<div class="brand-mark"><span class="dot"></span><span class="name">Amber Nook</span></div>

<!-- Light dashboard -->
<div class="dashboard light">
  <header class="topbar">
    <div class="logo-slot">Amber<br>Nook</div>
    <div class="greeting"><div class="hello">Hello, <b>Daniel Rhee</b></div><div class="sub">Welcome to Amber Nook</div></div>
    <div class="search">Search... <svg width="6" height="6" viewBox="0 0 12 12" fill="none" stroke="#6b7488" stroke-width="1.6"><circle cx="5" cy="5" r="3.5"/><path d="M8 8l3 3"/></svg></div>
    <div class="bell"><svg width="6" height="6" viewBox="0 0 12 12"><path d="M6 1a3.5 3.5 0 0 0-3.5 3.5V8L1.5 9.5h9L9.5 8V4.5A3.5 3.5 0 0 0 6 1zM4.8 10.5a1.2 1.2 0 0 0 2.4 0z" fill="#1c2a4a"/></svg></div>
    <div class="avatar" role="img" aria-label="User profile photo"></div>
    <div class="user-name">Daniel Rhee</div>
    <svg class="chev" width="6" height="5" viewBox="0 0 12 8" fill="none" stroke="#1c2a4a" stroke-width="1.6"><path d="M1 1l5 5 5-5"/></svg>
  </header>
  <nav class="sidebar">
    <div class="active-tick"></div>
    <div class="side-icon active" style="top:18px"><svg><use href="#i-grid"/></svg></div>
    <div class="side-icon" style="top:47px"><svg><use href="#i-pie"/></svg></div>
    <div class="side-icon" style="top:77px"><svg><use href="#i-cal"/></svg></div>
    <div class="side-icon" style="top:106px"><svg><use href="#i-doc"/></svg></div>
    <div class="side-icon" style="top:136px"><svg><use href="#i-box"/></svg></div>
    <div class="side-icon" style="top:165px"><svg><use href="#i-gear"/></svg></div>
    <div class="side-icon" style="top:334px"><svg><use href="#i-user"/></svg></div>
    <div class="side-icon" style="top:364px"><svg><use href="#i-power"/></svg></div>
  </nav>
  <main class="content">
    <section class="section">
      <div class="section-head"><h2 class="section-title">Self management</h2><span class="section-rule"></span><span class="progress"><svg width="8" height="5" viewBox="0 0 16 10" fill="none" stroke="#25a244" stroke-width="1.8"><path d="M1 6l4 3 9-8M10 1h4v4"/></svg>25%</span></div>
      <div class="cards">
        <div class="card"><span class="art" role="img" aria-label="Self-care illustration"></span><span class="label">Self-care and<br>well-being</span></div>
        <div class="card highlight"><span class="art" role="img" aria-label="Target illustration"></span><span class="label">Personal<br>development</span></div>
        <div class="card"><span class="art" role="img" aria-label="Calendar illustration"></span><span class="label">Hobbies and<br>interests</span></div>
        <div class="card"><span class="art" role="img" aria-label="Climbing steps illustration"></span><span class="label">Reflection and<br>journaling</span></div>
      </div>
    </section>
    <section class="section">
      <div class="section-head"><h2 class="section-title">Relationships management</h2><span class="section-rule"></span><span class="progress"><svg width="8" height="5" viewBox="0 0 16 10" fill="none" stroke="#25a244" stroke-width="1.8"><path d="M1 6l4 3 9-8M10 1h4v4"/></svg>70%</span></div>
      <div class="cards">
        <div class="card"><span class="art" role="img" aria-label="Social network illustration"></span><span class="label">Social<br>connections</span></div>
        <div class="card"><span class="art" role="img" aria-label="Phone message illustration"></span><span class="label">Communication</span></div>
        <div class="card"><span class="art" role="img" aria-label="Couple illustration"></span><span class="label">Relationship<br>goals</span></div>
        <div class="card"><span class="art" role="img" aria-label="Family illustration"></span><span class="label">Family<br>management</span></div>
      </div>
    </section>
    <section class="section">
      <div class="section-head"><h2 class="section-title">Career management</h2><span class="section-rule"></span><span class="progress"><svg width="8" height="5" viewBox="0 0 16 10" fill="none" stroke="#25a244" stroke-width="1.8"><path d="M1 6l4 3 9-8M10 1h4v4"/></svg>80%</span></div>
      <div class="cards">
        <div class="card"><span class="art" role="img" aria-label="Professional in gear illustration"></span><span class="label">Professional<br>development</span></div>
        <div class="card"><span class="art" role="img" aria-label="Job search screen illustration"></span><span class="label">Job search</span></div>
        <div class="card"><span class="art" role="img" aria-label="Performance chart illustration"></span><span class="label">Work performance</span></div>
        <div class="card"><span class="art" role="img" aria-label="Handshake illustration"></span><span class="label">Professional<br>relationships</span></div>
      </div>
    </section>
    <section class="section">
      <div class="section-head"><h2 class="section-title">Finance management</h2><span class="section-rule"></span><span class="progress"><svg width="8" height="5" viewBox="0 0 16 10" fill="none" stroke="#25a244" stroke-width="1.8"><path d="M1 6l4 3 9-8M10 1h4v4"/></svg>50%</span></div>
      <div class="cards">
        <div class="card"><span class="art" role="img" aria-label="Budget receipt illustration"></span><span class="label">Budgeting and<br>expense tracking</span></div>
        <div class="card"><span class="art" role="img" aria-label="Hand with coins illustration"></span><span class="label">Income<br>management</span></div>
        <div class="card"><span class="art" role="img" aria-label="Savings jar illustration"></span><span class="label">Saving and<br>investing</span></div>
        <div class="card"><span class="art" role="img" aria-label="Money bag illustration"></span><span class="label">Financial<br>health</span></div>
      </div>
    </section>
  </main>
  <footer class="footer">© 2024 Amber Nook. All rights reserved.</footer>
</div>

<!-- Branded dashboard -->
<div class="dashboard brand">
  <header class="topbar">
    <div class="logo-slot">Amber<br>Nook</div>
    <div class="greeting"><div class="hello">Hello, <b>Daniel Rhee</b></div><div class="sub">Welcome to Amber Nook</div></div>
    <div class="search">Search... <svg width="6" height="6" viewBox="0 0 12 12" fill="none" stroke="#ffffff" stroke-width="1.6"><circle cx="5" cy="5" r="3.5"/><path d="M8 8l3 3"/></svg></div>
    <div class="bell"><svg width="6" height="6" viewBox="0 0 12 12"><path d="M6 1a3.5 3.5 0 0 0-3.5 3.5V8L1.5 9.5h9L9.5 8V4.5A3.5 3.5 0 0 0 6 1zM4.8 10.5a1.2 1.2 0 0 0 2.4 0z" fill="#ffffff"/></svg></div>
    <div class="avatar" role="img" aria-label="User profile photo"></div>
    <div class="user-name">Daniel Rhee</div>
    <svg class="chev" width="6" height="5" viewBox="0 0 12 8" fill="none" stroke="#ffffff" stroke-width="1.6"><path d="M1 1l5 5 5-5"/></svg>
  </header>
  <nav class="sidebar">
    <div class="side-icon active" style="top:18px"><svg><use href="#i-grid"/></svg></div>
    <div class="side-icon" style="top:47px"><svg><use href="#i-pie"/></svg></div>
    <div class="side-icon" style="top:77px"><svg><use href="#i-cal"/></svg></div>
    <div class="side-icon" style="top:106px"><svg><use href="#i-doc"/></svg></div>
    <div class="side-icon" style="top:136px"><svg><use href="#i-box"/></svg></div>
    <div class="side-icon" style="top:165px"><svg><use href="#i-gear"/></svg></div>
    <div class="side-icon" style="top:334px"><svg><use href="#i-user"/></svg></div>
    <div class="side-icon" style="top:364px"><svg><use href="#i-power"/></svg></div>
  </nav>
  <main class="content">
    <section class="section">
      <div class="section-head"><h2 class="section-title">Self management</h2><span class="section-rule"></span><span class="progress"><svg width="8" height="5" viewBox="0 0 16 10" fill="none" stroke="#25a244" stroke-width="1.8"><path d="M1 6l4 3 9-8M10 1h4v4"/></svg>25%</span></div>
      <div class="cards">
        <div class="card"><span class="art" role="img" aria-label="Self-care illustration"></span><span class="label">Self-care and<br>well-being</span></div>
        <div class="card highlight"><span class="art" role="img" aria-label="Target illustration"></span><span class="label">Personal<br>development</span></div>
        <div class="card"><span class="art" role="img" aria-label="Calendar illustration"></span><span class="label">Hobbies and<br>interests</span></div>
        <div class="card"><span class="art" role="img" aria-label="Climbing steps illustration"></span><span class="label">Reflection and<br>journaling</span></div>
      </div>
    </section>
    <section class="section">
      <div class="section-head"><h2 class="section-title">Relationships management</h2><span class="section-rule"></span><span class="progress"><svg width="8" height="5" viewBox="0 0 16 10" fill="none" stroke="#25a244" stroke-width="1.8"><path d="M1 6l4 3 9-8M10 1h4v4"/></svg>70%</span></div>
      <div class="cards">
        <div class="card"><span class="art" role="img" aria-label="Social network illustration"></span><span class="label">Social<br>connections</span></div>
        <div class="card"><span class="art" role="img" aria-label="Phone message illustration"></span><span class="label">Communication</span></div>
        <div class="card"><span class="art" role="img" aria-label="Couple illustration"></span><span class="label">Relationship<br>goals</span></div>
        <div class="card"><span class="art" role="img" aria-label="Family illustration"></span><span class="label">Family<br>management</span></div>
      </div>
    </section>
    <section class="section">
      <div class="section-head"><h2 class="section-title">Career management</h2><span class="section-rule"></span><span class="progress"><svg width="8" height="5" viewBox="0 0 16 10" fill="none" stroke="#25a244" stroke-width="1.8"><path d="M1 6l4 3 9-8M10 1h4v4"/></svg>80%</span></div>
      <div class="cards">
        <div class="card"><span class="art" role="img" aria-label="Professional in gear illustration"></span><span class="label">Professional<br>development</span></div>
        <div class="card"><span class="art" role="img" aria-label="Job search screen illustration"></span><span class="label">Job search</span></div>
        <div class="card"><span class="art" role="img" aria-label="Performance chart illustration"></span><span class="label">Work performance</span></div>
        <div class="card"><span class="art" role="img" aria-label="Handshake illustration"></span><span class="label">Professional<br>relationships</span></div>
      </div>
    </section>
    <section class="section">
      <div class="section-head"><h2 class="section-title">Finance management</h2><span class="section-rule"></span><span class="progress"><svg width="8" height="5" viewBox="0 0 16 10" fill="none" stroke="#25a244" stroke-width="1.8"><path d="M1 6l4 3 9-8M10 1h4v4"/></svg>50%</span></div>
      <div class="cards">
        <div class="card"><span class="art" role="img" aria-label="Budget receipt illustration"></span><span class="label">Budgeting and<br>expense tracking</span></div>
        <div class="card"><span class="art" role="img" aria-label="Hand with coins illustration"></span><span class="label">Income<br>management</span></div>
        <div class="card"><span class="art" role="img" aria-label="Savings jar illustration"></span><span class="label">Saving and<br>investing</span></div>
        <div class="card"><span class="art" role="img" aria-label="Money bag illustration"></span><span class="label">Financial<br>health</span></div>
      </div>
    </section>
  </main>
  <footer class="footer">© 2024 Amber Nook. All rights reserved.</footer>
</div>
</body>
</html>
```